K & R Ground Works. Business card design

We need a business card designed for a new business. We have a bulldozer and tractor service. We clear land and make wildlife food plots. We provide disking, bush hogging, and site prep services.
I have attached an image of a business card that I like and would like my business cards to look similar.

Target Market(s)

anyone needing bulldozer and/or tractor services

Industry/Entity Type

Business

Contact Information for Business Card

K & R Ground Works, Operated by 7-T-Ranch
Dale Whitcomb
601-555-0148
dwk4821@mailbarn.example

Font styles to use
Sans Serif

Colors

Designer to choose colors to be used in the design.

Requirements
Must have
• image of tractor and bulldozer
• Land Clearing
• Wildlife food plots
• Bush Hogging
• Disking
• Site prep
Nice to have
• i have included a image of a business card that i like. I would like mine to be similar.

```html
<!DOCTYPE html>
<html lang="en">
<head>
<meta charset="utf-8">
<title>K &amp; R Ground Works – Business Card</title>
<link rel="stylesheet" href="https://fonts.googleapis.com/css2?family=Roboto:wght@400;500;700;900&display=swap">
<style>
  :root {
    --backdrop: #2e2e2e;
    --panel-top: #3a3a3a;
    --panel-bottom: #050505;
    --gold: #f6a623;
    --gold-bright: #ffc23a;
    --rust: #7a1410;
    --red: #a3201a;
    --silver: #d9d9d9;
    --text-light: #f2f2f2;
  }
  * { margin: 0; padding: 0; box-sizing: border-box; }
  html, body {
    width: 1200px; height: 900px; overflow: hidden;
    background: var(--backdrop);
    font-family: "Roboto", sans-serif;
  }
  .card {
    position: absolute; left: 50px; top: 149px;
    width: 1100px; height: 602px;
    overflow: hidden;
    box-shadow: 0 6px 18px rgba(0,0,0,.5);
    background: var(--panel-bottom);
  }
  .photo {
    position: absolute; left: 0; top: 0; width: 1100px; height: 356px;
    background:
      linear-gradient(90deg,
        #2c4b7a 0%, #3d5e86 10%, #c9a21a 24%, #e2b624 42%, #9c8a5a 55%,
        #6d8a3d 64%, #d2481f 72%, #e4562a 84%, #4f7a2e 94%, #3d6b28 100%);
  }
  .photo::after {
    content: ""; position: absolute; inset: 0;
    background: linear-gradient(180deg, rgba(255,255,255,.06) 0%, rgba(0,0,0,0) 50%, rgba(40,30,10,.25) 100%);
  }
  .brand-band {
    position: absolute; left: 0; top: 228px; width: 820px; height: 128px;
    background: linear-gradient(90deg, rgba(0,0,0,.82) 0%, rgba(0,0,0,.75) 62%, rgba(0,0,0,0) 100%);
  }
  .brand-name {
    position: absolute; left: 48px; top: 240px;
    font-weight: 900; font-size: 50px; letter-spacing: 1px;
    color: var(--text-light); text-transform: uppercase;
    line-height: 1;
  }
  .brand-tagline {
    position: absolute; left: 50px; top: 314px;
    font-weight: 500; font-size: 17px; letter-spacing: 8.6px;
    color: var(--text-light); text-transform: uppercase;
  }
  .divider {
    position: absolute; left: 0; top: 356px; width: 1100px; height: 10px;
    background: linear-gradient(90deg, var(--rust), var(--red) 25%, var(--gold-bright) 50%, var(--red) 75%, var(--rust));
  }
  .info-panel {
    position: absolute; left: 0; top: 366px; width: 1100px; height: 190px;
    background: linear-gradient(180deg, var(--panel-top) 0%, #151515 45%, var(--panel-bottom) 100%);
  }
  .person-name {
    position: absolute; left: 48px; top: 404px;
    font-size: 47px; line-height: 1; color: var(--gold);
    text-transform: uppercase; letter-spacing: 1px;
  }
  .person-name .first { font-weight: 900; margin-right: 18px; }
  .person-name .last { font-weight: 400; }
  .contact {
    position: absolute; left: 48px;
    display: flex; align-items: center; gap: 14px;
    font-size: 28px; color: var(--text-light);
  }
  .contact svg { width: 28px; height: 28px; }
  .contact.email { top: 455px; }
  .contact.phone { top: 496px; }
  .services {
    position: absolute; left: 758px; top: 385px;
    list-style: none; color: var(--text-light);
    font-size: 28px; line-height: 37.5px;
  }
  .services li { display: flex; align-items: center; gap: 10px; }
  .services svg { width: 20px; height: 20px; flex: none; }
  .services .gap { margin-left: 10px; }
  .bottom-band {
    position: absolute; left: 0; top: 556px; width: 1100px; height: 46px;
    background: linear-gradient(90deg, var(--rust), var(--red) 25%, var(--gold-bright) 50%, var(--red) 75%, var(--rust));
    border-top: 5px solid var(--silver);
  }
  .bottom-band::after {
    content: ""; position: absolute; inset: 0;
    background: linear-gradient(180deg, rgba(255,255,255,.15), rgba(0,0,0,.35));
  }
</style>
</head>
<body>
  <div class="card">
    <div class="photo" role="img" aria-label="Photo of a yellow bulldozer on a dirt slope and a red tractor with front loader in green grass"></div>
    <div class="brand-band"></div>
    <div class="brand-name">K &amp; R Ground Works</div>
    <div class="brand-tagline">Operated by 7-T-Ranch</div>
    <div class="divider"></div>

    <div class="info-panel"></div>
    <div class="person-name"><span class="first">Dale</span><span class="last">Whitcomb</span></div>
    <div class="contact email">
      <svg viewBox="0 0 28 28" fill="none" stroke="#f6a623" stroke-width="2">
        <rect x="3" y="7" width="22" height="15" rx="1"/>
        <path d="M3 8 L14 16 L25 8"/>
      </svg>
      <span>dwk4821@mailbarn.example</span>
    </div>
    <div class="contact phone">
      <svg viewBox="0 0 28 28" fill="none" stroke="#f6a623" stroke-width="2" stroke-linejoin="round">
        <path d="M8 4 L11 4 L13 10 L10 12 C11 15 13 17 16 18 L18 15 L24 17 L24 20 C24 22 22 24 20 24 C12 23 5 16 4 8 C4 6 6 4 8 4 Z"/>
      </svg>
      <span>601-555-0148</span>
    </div>

    <ul class="services">
      <li><svg viewBox="0 0 20 20"><path d="M2 3 L18 10 L2 17 L7 10 Z" fill="#f6a623"/></svg>Land Clearing</li>
      <li><svg viewBox="0 0 20 20"><path d="M2 3 L18 10 L2 17 L7 10 Z" fill="#f6a623"/></svg>Wildlife food plots</li>
      <li><svg viewBox="0 0 20 20"><path d="M2 3 L18 10 L2 17 L7 10 Z" fill="#f6a623"/></svg>Bush Hogging</li>
      <li><svg viewBox="0 0 20 20"><path d="M2 3 L18 10 L2 17 L7 10 Z" fill="#f6a623"/></svg>Disking<svg class="gap" viewBox="0 0 20 20"><path d="M2 3 L18 10 L2 17 L7 10 Z" fill="#f6a623"/></svg>Site prep</li>
    </ul>

    <div class="bottom-band"></div>
  </div>
</body>
</html>
```